Harborline Quoting
Business Cards and Stationery for Service Co
Simple
Dane Corwell
Vice President
20436 SW 47th Avenue Suite 3105 Vancouver, WA 97531
danec@harborlinequoting.com
www.harborlinequoting.com
Please keep it simple and professional.
Just the logo

```html
<!DOCTYPE html>
<html lang="en">
<head>
<meta charset="utf-8">
<title>Harborline Quoting – Business Cards</title>
<link rel="stylesheet" href="https://fonts.googleapis.com/css2?family=Montserrat:wght@600;700&family=Open+Sans:wght@400;600&display=swap">
<style>
  :root {
    --brand-orange: #e0562f;
    --card-white: #ffffff;
    --ink-grey: #4a4a4a;
    --backdrop: #e9e7e3;
    --card-shadow: rgba(0, 0, 0, 0.18);
  }
  * { box-sizing: border-box; margin: 0; padding: 0; }
  html, body { width: 1200px; height: 904px; overflow: hidden; }
  body {
    background: var(--backdrop);
    font-family: "Open Sans", sans-serif;
    display: flex;
    flex-direction: column;
    align-items: center;
    justify-content: center;
    gap: 40px;
  }
  .card {
    width: 680px;
    height: 389px;
    border-radius: 18px;
    position: relative;
    overflow: hidden;
    box-shadow: 0 10px 28px var(--card-shadow);
  }

  /* Back of card */
  .card-back {
    background: var(--brand-orange);
    display: flex;
    align-items: center;
    justify-content: center;
    gap: 18px;
  }
  .card-back .brand-dot {
    width: 62px; height: 62px;
    border-radius: 50%;
    background: var(--card-white);
  }
  .card-back .brand-name {
    font-family: "Montserrat", sans-serif;
    font-weight: 700;
    font-size: 34px;
    letter-spacing: 1px;
    color: var(--card-white);
    text-transform: uppercase;
  }

  /* Front of card */
  .card-front { background: var(--card-white); }
  .front-brand {
    position: absolute;
    left: 44px; top: 40px;
    display: flex;
    align-items: center;
    gap: 12px;
    z-index: 1;
  }
  .front-brand .brand-dot {
    width: 44px; height: 44px;
    border-radius: 50%;
    background: var(--brand-orange);
    flex: none;
  }
  .front-brand .brand-name {
    font-family: "Montserrat", sans-serif;
    font-weight: 700;
    font-size: 22px;
    line-height: 1.1;
    letter-spacing: 1px;
    color: var(--brand-orange);
    text-transform: uppercase;
  }
  .accent-disc {
    position: absolute;
    right: -170px; top: -40px;
    width: 470px; height: 470px;
    border-radius: 50%;
    background: var(--brand-orange);
  }
  .name-tag {
    position: absolute;
    right: 44px; top: 130px;
    background: var(--brand-orange);
    border: 2px solid var(--card-white);
    padding: 10px 22px;
    text-align: center;
    color: var(--card-white);
    white-space: nowrap;
  }
  .name-tag .person-name {
    font-family: "Montserrat", sans-serif;
    font-weight: 600;
    font-size: 20px;
  }
  .name-tag .person-title {
    font-size: 14px;
    margin-top: 2px;
  }
  .contact-block {
    position: absolute;
    left: 44px; bottom: 36px;
    color: var(--ink-grey);
    font-size: 14px;
    line-height: 1.55;
  }
  .contact-block .address { margin-bottom: 8px; }
  .contact-line {
    display: flex;
    align-items: center;
    gap: 10px;
  }
  .contact-line svg { width: 14px; height: 14px; flex: none; }
</style>
</head>
<body>

  <section class="card card-back" aria-label="Back of business card">
    <span class="brand-dot"></span>
    <span class="brand-name">Harborline Quoting</span>
  </section>

  <section class="card card-front" aria-label="Front of business card">
    <div class="accent-disc"></div>

    <div class="front-brand">
      <span class="brand-dot"></span>
      <span class="brand-name">Harborline<br>Quoting</span>
    </div>

    <div class="name-tag">
      <div class="person-name">Dane Corwell</div>
      <div class="person-title">Vice President</div>
    </div>

    <div class="contact-block">
      <div class="address">20436 SW 47th Avenue<br>Suite 3105</div>
      <div class="contact-line">
        <svg viewBox="0 0 16 16" aria-hidden="true"><path fill="#e0562f" d="M3.5 1.5l2.5 0 1 3.5-1.7 1.2a8 8 0 0 0 4.5 4.5l1.2-1.7 3.5 1v2.5c0 .8-.7 1.5-1.5 1.5A12.5 12.5 0 0 1 2 3c0-.8.7-1.5 1.5-1.5z"/></svg>
        <span>360-555-0148</span>
      </div>
      <div class="contact-line">
        <svg viewBox="0 0 16 16" aria-hidden="true"><rect x="2" y="4" width="12" height="9" rx="1.5" fill="#e0562f"/><rect x="4" y="2" width="8" height="4" fill="#e0562f"/><rect x="4.5" y="8" width="7" height="1.2" fill="#fff"/></svg>
        <span>888-555-0172</span>
      </div>
      <div class="contact-line">
        <svg viewBox="0 0 16 16" aria-hidden="true"><rect x="1.5" y="3.5" width="13" height="9" rx="1.2" fill="#e0562f"/><path d="M2 4.5l6 4.5 6-4.5" fill="none" stroke="#fff" stroke-width="1.2"/></svg>
        <span>danec@harborlinequoting.com</span>
      </div>
      <div class="contact-line">
        <svg viewBox="0 0 16 16" aria-hidden="true"><circle cx="8" cy="8" r="6.5" fill="#e0562f"/><path d="M1.5 8h13M8 1.5c-2.5 3-2.5 10 0 13M8 1.5c2.5 3 2.5 10 0 13" fill="none" stroke="#fff" stroke-width="0.9"/></svg>
        <span>www.harborlinequoting.com</span>
      </div>
    </div>
  </section>

</body>
</html>
```